Biker App Design
Zielgruppe
VeloMarn erstellt eine App für Biker mit der:
- Motorradfahrer andere Biker finden können um gemeinsam zu fahren
- Motorradfahrer ihre Strecke tracken können um Punkte zu sammeln
- Biker können mit diesen Punkten Ränge aufsteigen 'Masterbiker, Anfänger, GuruFahrer, etc.', es soll eine Art 'Erfahrungsleiste' angezeigt werden
- Diese Punkte können gegen Gutscheine/Wertsachen eingelöst werden
- Es gibt Nachrichten (Art Blogeinträge) genau zu diesen Themen
Aufgabenstellung
Modernes Design
Reduziert
Es werden folgende Screens benötigt:
Startbild
Start - Dateneintragen:
Um den Fahrer besser mit anderen Fahren zu verknüpfen muss er folgende informationen angeben:
- Welche Art Motorrad fährt er? Sport, Vintage, Cross
- Männlich/Weiblich/Divers
- Geburtsjahr
- PLZ des Heimatorts
- Nickname
Startscreen um andere Biker zu suchen und damit eine Tour zu starten
- Hier sollte ein 'Map' Bild mit einem Kreis für den Umkreis dargestellt werden + Pins mit Personenbilder , welche
Personen in der Nähe sind und auch fahren möchten
- Hier sollte stehen, wieviel Punkte er noch benötigt um den nächsten Gutschein freizuschalten
Screen zum Start des Trackens
Screen während dem Tracken mit Pause/Stop-Option
Screen mit einem Überblick der neuen Blogeinträge
Screen beim beenden des Trackens (Strecke speichern, Bild hinzufügen, Freunde informieren ich bin angekommen)
Screen Profilseite, Bild des Bikers + Bike + Erfahrungspunkte + gesammelte Errungenschaften z.B. 'Mit 3 Freunden mehr als 1000km gefahren'
Screen Bestenliste, anhand der Punkte
Es sollen Dateiformate verwendet werden, die gut wiederverwendet werden können. Es sollen sich Bausteine aus diesen Design wiederverwenden lassen können.
Wir benötigen eine APP mit einem User-Dashboards (Life-Account) in dem Finanz, Karriere und Gesundheitsthemen erkennbar sein sollen. Look and Feel soll seriös, schnörkelos und modern sein.
Das Design soll simpel sein. Also Verwendung von wenigen, dezenten Farben (Schattierungen / Blendeffekte erlaubt) und san-serife / simple schrift. Ich würde es mit progressiv, technisch, eher jugendlich, eher offen/frisch, modern, eher prägnant, clean, urban, eher freundschaftlich, schlicht, ehe..
hallo, wir brauchen das design für eine startseite. thema taxi app alle weiteren infos siehe anhang pdf eilauftrag - sofort kauf möglich danke
Unter Flickhafen.de kann das aktuelle Design angeschaut werden. Die Farbe sollten übernommen werden. Über die Startseite kann der Kunde sein Gerät, Service sowie seine Adresse eingeben. Auf der Vergleichsseite bekommt der Kunde die Übersicht welche Reparaturwerkstätten es gibt, zu welch..
Vorweg: Dem Auftrag folgen weitere Teilaufträge an den Gewinner, natürlich gegen Bezahlung. Für die bereits programmierte Webapplikation "tocks" wird ein Design benötigt. Tocks ähnelt den bereits bestehenden Zeiterfassungssystemen, soll sich aber anhand von Einfachheit, Speditivität und..

```html
<!DOCTYPE html>
<html lang="de">
<head>
<meta charset="utf-8">
<title>Kradpfad – App Screens</title>
<link href="https://fonts.googleapis.com/css2?family=Fira+Sans:wght@300;400;600;700;800&display=swap" rel="stylesheet">
<style>
:root{
  --page:#ffffff;
  --bar:#1f1a17;
  --panel:#e9e9e9;
  --card:#ffffff;
  --ink:#222222;
  --muted:#9a9a9a;
  --line:#cfcfcf;
  --dark-btn:#5f5f5f;
  --light-btn:#e4e4e4;
  --map:#f1c98c;
  --map-deep:#e2b57a;
  --accent:#8a5a2b;
  --progress:#6d6d6d;
  --progress-rest:#c8c8c8;
}
*{box-sizing:border-box;margin:0;padding:0}
html,body{width:816px;height:1200px;overflow:hidden;background:var(--page)}
body{position:relative;font-family:"Fira Sans",Arial,sans-serif;color:var(--ink)}
.icons{position:absolute;width:0;height:0}

.screen{position:absolute;width:138px;height:246px;overflow:hidden;background:var(--panel);box-shadow:2px 3px 5px rgba(0,0,0,.25)}
.app-bar{position:absolute;left:0;top:0;width:100%;height:23px;background:var(--bar);color:#fff;display:flex;align-items:center;justify-content:center;font-size:4.2px;font-weight:700;letter-spacing:.1px}
.app-bar .menu{position:absolute;left:7px;top:8px;width:7px}
.app-bar .user{position:absolute;right:6px;top:6px;width:10px;height:10px;fill:#fff}

/* splash */
.splash{left:216px;top:85px;width:150px;height:327px;border-radius:18px;overflow:hidden}
.splash-photo{position:absolute;inset:0;background:linear-gradient(180deg,#c9b98a 0%,#8a7a3a 22%,#6b6a2c 38%,#8d8a78 52%,#4b4640 70%,#1d1b19 100%)}
.status-bar{position:absolute;left:14px;top:7px;font-size:5.5px;color:#fff}
.brand-name{position:absolute;left:0;right:0;top:60px;text-align:center;color:#111;font-size:24px;font-weight:700;letter-spacing:1px;line-height:28px}

/* create profile */
.setup{left:421px;top:170px}
.setup h1{position:absolute;left:6px;top:36px;font-size:7px;font-weight:700;color:var(--ink)}
.field{position:absolute;left:6px;width:125px;height:19px;background:var(--card);display:flex;align-items:center;justify-content:space-between;padding:0 6px;font-size:4.3px;color:var(--muted)}
.field small{font-size:3px;color:#777}
.pill-next{position:absolute;left:6px;top:218px;width:125px;height:18px;border-radius:9px;background:var(--dark-btn);display:flex;align-items:center;justify-content:center}

/* map screens */
.map{position:absolute;left:0;top:23px;width:100%;height:223px;background:linear-gradient(135deg,var(--map) 0%,#f4d29e 50%,var(--map) 100%)}
.radius{position:absolute;left:6px;top:30px;width:126px;height:126px;border-radius:50%;background:rgba(180,140,90,.22)}
.pin{position:absolute;width:20px;height:25px}
.pin-label{position:absolute;background:#fff;border-radius:3px;padding:1px 3px;font-size:2.6px;font-weight:700;line-height:3px}
.pin-label i{display:block;font-style:normal;font-weight:400;font-size:2px;color:var(--muted)}
.center-dot{position:absolute;width:8px;height:8px;border-radius:50%;background:#6a6a6a}
.sun{position:absolute;width:13px;height:13px;border-radius:50%;background:#f9d79e}

.card{position:absolute;background:var(--card)}
.label{font-size:4.2px;font-weight:700}
.sub{font-size:3.3px;color:#555}
.tiny{font-size:2.4px;color:var(--muted)}
.progress{position:relative;height:4px;background:var(--progress-rest)}
.progress span{position:absolute;left:0;top:0;bottom:0;background:var(--progress)}
.round-btn{position:absolute;width:15px;height:15px;border-radius:50%;background:var(--dark-btn);display:flex;align-items:center;justify-content:center}
.cta-text{position:absolute;font-size:4px;font-weight:600}
.input{position:absolute;height:12px;border:.8px solid #777;display:flex;align-items:center;justify-content:space-between;padding:0 5px;font-size:4.2px;color:var(--muted);background:#fff}
.input small{font-size:2.8px;color:#666}
.btn{position:absolute;height:12px;border-radius:6px;display:flex;align-items:center;justify-content:center;font-size:4px;font-weight:600}
.btn.dark{background:var(--dark-btn);color:#fff}
.btn.light{background:var(--light-btn);color:#555}
.photo{position:absolute;background:linear-gradient(160deg,#f2dcc0 0%,#d9a878 35%,#7a5a3e 65%,#3a2c22 100%)}

.s-map1{left:90px;top:483px}
.s-map2{left:253px;top:483px}
.s-map3{left:421px;top:483px}
.s-map4{left:588px;top:483px}

.timer{position:absolute;left:0;right:0;top:17px;text-align:center;font-size:13px;font-weight:600;letter-spacing:.2px}
.timer-units{position:absolute;left:0;right:0;top:32px;display:flex;justify-content:center;gap:5px;font-size:2.8px;color:#666}

/* row 3 */
.s-profile{left:90px;top:800px}
.s-blog{left:253px;top:800px}
.s-best{left:421px;top:800px}
.app-bar.split{width:115px}
.avatar-slot{position:absolute;right:0;top:0;width:23px;height:23px;background:#e2e2e2;display:flex;align-items:center;justify-content:center}
.avatar{position:absolute;left:8px;top:7px;width:48px;height:48px;border-radius:50%;background:#e6e6e6;display:flex;align-items:center;justify-content:center}
.badges{position:absolute;left:7px;top:16px;display:flex;gap:7px}
.badge{width:13px;display:flex;flex-direction:column;align-items:center;gap:2px}
.badge b{width:12px;height:12px;border-radius:50%;display:block}
.badge span{font-size:1.6px;color:var(--muted);text-align:center;line-height:1.9px}

.blog-card{position:absolute;left:5px;width:128px;background:#e6e6e6}
.blog-title{position:absolute;left:13px;font-size:4.6px;font-weight:800;letter-spacing:.1px}
.blog-text{position:absolute;left:13px;width:104px;font-size:4.5px;line-height:9px;color:#666;font-weight:300}
.author{position:absolute;left:0;top:137px;width:128px;height:31px;background:var(--accent);color:#fff;display:flex;align-items:center;justify-content:space-between;padding:0 7px 0 13px;font-size:4.3px;font-weight:700}
.author small{font-size:3px;font-weight:400}

.rank-head{position:absolute;top:37px;left:10px;right:20px;font-size:4px;font-weight:700;display:flex}
.rank-list{position:absolute;left:5px;top:47px;width:128px;height:199px;background:#fff}
.rank-row{position:absolute;left:0;width:100%;height:20px;font-size:4.6px}
.rank-row .pos{position:absolute;left:6px;top:7px;font-weight:600}
.rank-row .name{position:absolute;left:25px;top:3px;font-size:4px;font-weight:700;line-height:4.5px}
.rank-row .name i{display:block;font-style:normal;font-weight:400;font-size:3px;color:#666}
.rank-row .face{position:absolute;left:63px;top:2px;width:13px;height:13px;border-radius:50%;background:#ececec;display:flex;align-items:center;justify-content:center}
.rank-row .pts{position:absolute;left:100px;top:7px;color:#555}
</style>
</head>
<body>

<svg class="icons" aria-hidden="true">
  <symbol id="person" viewBox="0 0 20 20"><circle cx="10" cy="6" r="4.5"/><path d="M2 19c0-5 3.6-7.5 8-7.5s8 2.5 8 7.5z"/></symbol>
  <symbol id="menu" viewBox="0 0 10 8"><path d="M0 1h10M0 4h8M0 7h5" stroke="#fff" stroke-width="1.1"/></symbol>
  <symbol id="arrow-right" viewBox="0 0 10 10"><path d="M1 5h8M5.5 1.5 9 5 5.5 8.5" fill="none" stroke="#fff" stroke-width="1.1"/></symbol>
  <symbol id="arrow-left" viewBox="0 0 10 10"><path d="M9 5H1M4.5 1.5 1 5l3.5 3.5" fill="none" stroke="#fff" stroke-width="1.1"/></symbol>
  <symbol id="pin" viewBox="0 0 20 25"><path d="M10 0a10 10 0 0 1 10 10c0 6-10 15-10 15S0 16 0 10A10 10 0 0 1 10 0z" fill="#6a6a6a"/><circle cx="10" cy="10" r="7" fill="#fff"/><g fill="#6a6a6a" transform="translate(5 5) scale(.5)"><circle cx="10" cy="6" r="4.5"/><path d="M2 19c0-5 3.6-7.5 8-7.5s8 2.5 8 7.5z"/></g></symbol>
</svg>

<!-- Splash -->
<section class="screen splash">
  <div class="splash-photo" role="img" aria-label="Foto: Blick über Motorradlenker und Tacho auf eine Landstraße im Wald bei Sonnenuntergang"></div>
  <div class="status-bar">9:30</div>
  <div class="brand-name">KRADPFAD</div>
</section>

<!-- Create profile -->
<section class="screen setup">
  <h1>Erstelle Dein Profil</h1>
  <div class="field" style="top:58px">Biker01<small>Nickname</small></div>
  <div class="field" style="top:83px">Männlich/Weiblich/Divers<small>Geschlecht</small></div>
  <div class="field" style="top:108px">09.09.1987<small>Geburtsjahr</small></div>
  <div class="field" style="top:133px">46535<small>PLZ des Heimatorts</small></div>
  <div class="field" style="top:158px">Sport/Vintage/Cross<small>Motorradart</small></div>
  <div class="pill-next"><svg width="7" height="7"><use href="#arrow-right"/></svg></div>
</section>

<!-- Map: find bikers -->
<section class="screen s-map1">
  <div class="map" role="img" aria-label="Stadtplan der Umgebung in Sandtönen"></div>
  <div class="radius"></div>
  <div class="sun" style="left:122px;top:50px"></div>
  <div class="center-dot" style="left:65px;top:86px"></div>
  <svg class="pin" style="left:28px;top:39px"><use href="#pin"/></svg>
  <div class="pin-label" style="left:45px;top:39px">Steffi36<i>Anfänger</i></div>
  <svg class="pin" style="left:22px;top:105px"><use href="#pin"/></svg>
  <div class="pin-label" style="left:39px;top:104px">Heiko7<i>Anfänger</i></div>
  <svg class="pin" style="left:93px;top:99px"><use href="#pin"/></svg>
  <div class="pin-label" style="left:110px;top:98px">Jürgen<i>Masterbiker</i></div>
  <div class="card" style="left:6px;top:167px;width:125px;height:71px">
    <div class="label" style="position:absolute;left:7px;top:7px">Mein Status</div>
    <div class="sub" style="position:absolute;left:7px;top:12px">Anfänger</div>
    <div class="tiny" style="position:absolute;left:7px;top:17px">noch 25 Punkte</div>
    <div class="progress" style="position:absolute;left:7px;top:23px;width:89px"><span style="width:66px"></span></div>
    <div class="tiny" style="position:absolute;left:7px;top:30px">75/100</div>
    <div class="tiny" style="position:absolute;left:85px;top:30px">Freischalten</div>
    <div class="tiny" style="position:absolute;left:102px;top:27px;width:20px;line-height:2.6px">Gutschein Reifenwechsel</div>
    <div class="cta-text" style="left:50px;top:58px">Starte deine Strecke!</div>
    <div class="round-btn" style="left:98px;top:53px"><svg width="7" height="7"><use href="#arrow-right"/></svg></div>
  </div>
  <div class="app-bar"><svg class="menu" height="6"><use href="#menu"/></svg>BIKER-MAP<svg class="user"><use href="#person"/></svg></div>
</section>

<!-- Map: start route -->
<section class="screen s-map2">
  <div class="map" role="img" aria-label="Stadtplan der Umgebung in Sandtönen"></div>
  <div class="radius"></div>
  <div class="sun" style="left:122px;top:50px"></div>
  <div class="center-dot" style="left:65px;top:86px"></div>
  <svg class="pin" style="left:28px;top:39px"><use href="#pin"/></svg>
  <div class="pin-label" style="left:45px;top:39px">Steffi36<i>Anfänger</i></div>
  <svg class="pin" style="left:22px;top:105px"><use href="#pin"/></svg>
  <div class="pin-label" style="left:39px;top:104px">Heiko7<i>Anfänger</i></div>
  <svg class="pin" style="left:93px;top:99px"><use href="#pin"/></svg>
  <div class="pin-label" style="left:110px;top:98px">Jürgen<i>Masterbiker</i></div>
  <div class="card" style="left:6px;top:119px;width:125px;height:119px">
    <div class="label" style="position:absolute;left:7px;top:17px">Starte deine Strecke</div>
    <div class="input" style="left:7px;top:27px;width:94px">Mein Standort<small>Start</small></div>
    <div class="input" style="left:7px;top:44px;width:94px">Jürgen<small>Mitfahrer</small></div>
    <svg style="position:absolute;left:106px;top:46px" width="9" height="9" viewBox="0 0 9 9"><circle cx="4.5" cy="4.5" r="4.5" fill="#5f5f5f"/><path d="M4.5 2.3v4.4M2.3 4.5h4.4" stroke="#fff" stroke-width=".8"/></svg>
    <div style="position:absolute;left:7px;top:63px;width:94px;height:14px;background:var(--panel);font-size:3.8px;font-weight:700;padding:4px 8px">Heiko7 <span style="font-weight:400;font-size:3px">Anfänger</span></div>
    <div class="cta-text" style="left:75px;top:102px">Los gehts!</div>
    <div class="round-btn" style="left:104px;top:98px"><svg width="7" height="7"><use href="#arrow-right"/></svg></div>
  </div>
  <div class="app-bar"><svg class="menu" height="6"><use href="#menu"/></svg>BIKER-MAP<svg class="user"><use href="#person"/></svg></div>
</section>

<!-- Map: tracking -->
<section class="screen s-map3">
  <div class="map" role="img" aria-label="Stadtplan mit gefahrener Strecke"></div>
  <div class="sun" style="left:122px;top:50px"></div>
  <svg style="position:absolute;left:0;top:0" width="138" height="246"><polyline points="15,126 22,103 48,99 41,65 105,57" fill="none" stroke="#6a6a6a" stroke-width="2.2"/><circle cx="15" cy="126" r="3.5" fill="#6a6a6a"/></svg>
  <div class="card" style="left:6px;top:167px;width:125px;height:79px">
    <div class="timer">00:37:21</div>
    <div class="timer-units"><span>Stunden</span><span>Minuten</span><span>Sekunden</span></div>
    <div class="btn light" style="left:9px;top:54px;width:35px">Pause</div>
    <div class="btn dark" style="left:82px;top:54px;width:35px">Beenden</div>
  </div>
  <div class="app-bar"><svg class="menu" height="6"><use href="#menu"/></svg>BIKER-MAP<svg class="user"><use href="#person"/></svg></div>
</section>

<!-- Map: arrival -->
<section class="screen s-map4">
  <div class="map" role="img" aria-label="Stadtplan der Umgebung in Sandtönen"></div>
  <div class="card" style="left:6px;top:33px;width:125px;height:213px">
    <div class="label" style="position:absolute;left:7px;top:11px">Meine Strecke</div>
    <div class="sub" style="position:absolute;left:7px;top:16px">67 km/h</div>
    <div class="progress" style="position:absolute;left:7px;top:26px;width:89px"><span style="width:66px"></span></div>
    <div class="tiny" style="position:absolute;left:7px;top:33px">89/100</div>
    <div class="tiny" style="position:absolute;left:83px;top:33px">Freischalten</div>
    <div class="tiny" style="position:absolute;left:104px;top:32px;width:20px;line-height:2.6px">Gutschein Reifenwechsel</div>
    <div class="photo" style="left:7px;top:46px;width:111px;height:67px" role="img" aria-label="Foto: zwei Biker mit Motorrädern in hügeliger Landschaft im Abendlicht"></div>
    <div class="label" style="position:absolute;left:7px;top:121px">Mitfahrer</div>
    <div class="sub" style="position:absolute;left:7px;top:126px">Heiko7</div>
    <div class="label" style="position:absolute;left:7px;top:138px">Ankunft senden an</div>
    <div class="input" style="left:7px;top:148px;width:63px">Jürgen, etc..</div>
    <div class="btn light" style="left:82px;top:148px;width:36px;height:13px">Senden</div>
    <div class="round-btn" style="left:7px;top:189px"><svg width="7" height="7"><use href="#arrow-left"/></svg></div>
    <div class="btn dark" style="left:83px;top:190px;width:36px;height:14px">Speichern</div>
  </div>
  <div class="app-bar"><svg class="menu" height="6"><use href="#menu"/></svg>BIKER-MAP<svg class="user"><use href="#person"/></svg></div>
</section>

<!-- Profile -->
<section class="screen s-profile">
  <div class="app-bar split"><svg class="menu" height="6"><use href="#menu"/></svg>PROFIL</div>
  <div class="avatar-slot"><svg width="10" height="10" style="fill:#fff"><use href="#person"/></svg></div>
  <div class="card" style="left:6px;top:30px;width:125px;height:63px">
    <div class="avatar"><svg width="28" height="28" style="fill:#fff"><use href="#person"/></svg></div>
    <div class="label" style="position:absolute;left:70px;top:24px">Nickname</div>
    <div class="tiny" style="position:absolute;left:70px;top:29px;color:#555">Biker01</div>
    <div class="label" style="position:absolute;left:70px;top:36px">Motorrad</div>
    <div class="tiny" style="position:absolute;left:70px;top:41px;color:#555">Cross</div>
  </div>
  <div class="card" style="left:6px;top:100px;width:125px;height:40px">
    <div class="label" style="position:absolute;left:7px;top:7px">Meine Status</div>
    <div class="sub" style="position:absolute;left:7px;top:12px">Anfänger</div>
    <div class="progress" style="position:absolute;left:7px;top:21px;width:89px"><span style="width:66px"></span></div>
    <div class="tiny" style="position:absolute;left:7px;top:28px">89/100</div>
    <div class="tiny" style="position:absolute;left:85px;top:28px">Freischalten</div>
    <div class="tiny" style="position:absolute;left:102px;top:27px;width:20px;line-height:2.6px">Gutschein Reifenwechsel</div>
  </div>
  <div class="card" style="left:6px;top:148px;width:125px;height:41px">
    <div class="label" style="position:absolute;left:7px;top:7px">Meine Errungenschaften</div>
    <div class="badges">
      <div class="badge"><b style="background:#6a6a6a"></b><span>Gutschein eingelöst</span></div>
      <div class="badge"><b style="background:#555"></b><span>Gesamte Umgebung</span></div>
      <div class="badge"><b style="background:#555"></b><span>Tour mit Freunden</span></div>
      <div class="badge"><b style="background:#d6d6d6"></b><span>Stufe Level</span></div>
      <div class="badge"><b style="background:#d6d6d6"></b><span>Tour mit Freunden</span></div>
      <div class="badge"><b style="background:#d6d6d6"></b><span>1000 km gefahren</span></div>
    </div>
  </div>
  <div class="card" style="left:6px;top:197px;width:125px;height:49px">
    <div class="label" style="position:absolute;left:7px;top:7px">Letztes Update</div>
    <div class="photo" style="left:7px;top:16px;width:111px;height:33px" role="img" aria-label="Foto: Biker mit Motorrädern im Abendlicht"></div>
  </div>
</section>

<!-- Blog -->
<section class="screen s-blog">
  <div class="app-bar"><svg class="menu" height="6"><use href="#menu"/></svg>BLOG<svg class="user"><use href="#person"/></svg></div>
  <div class="blog-card" style="top:30px;height:168px">
    <div class="blog-title" style="top:13px">NEUSTE STRECKE</div>
    <div class="photo" style="left:8px;top:25px;width:111px;height:67px" role="img" aria-label="Foto: zwei Biker mit Motorrädern in hügeliger Landschaft im Abendlicht"></div>
    <div class="blog-text" style="top:101px">Excepteur sint occaecat cupidatat non proident, sunt in culpa qui officia deserunt</div>
    <div class="author">von Biker01<small>vor einer Stunde</small></div>
  </div>
  <div class="blog-card" style="top:205px;height:41px">
    <div class="blog-title" style="top:13px">LOREM IPSUM</div>
    <div class="photo" style="left:8px;top:27px;width:111px;height:14px" role="img" aria-label="Foto: Biker im Abendlicht"></div>
  </div>
</section>

<!-- Leaderboard -->
<section class="screen s-best">
  <div class="app-bar"><svg class="menu" height="6"><use href="#menu"/></svg>BESTENLISTE<svg class="user"><use href="#person"/></svg></div>
  <div class="rank-head"><span style="width:20px">Platz</span><span style="width:73px">Nickname</span><span>Punkte</span></div>
  <div class="rank-list">
    <div class="rank-row" style="top:12px"><span class="pos">1.</span><span class="name">Jürgen<i>Masterbiker</i></span><span class="face"><svg width="7" height="7" style="fill:#fff"><use href="#person"/></svg></span><span class="pts">567</span></div>
    <div class="rank-row" style="top:37px"><span class="pos">2.</span><span class="name">Heiko<i>Masterbiker</i></span><span class="face"><svg width="7" height="7" style="fill:#fff"><use href="#person"/></svg></span><span class="pts">456</span></div>
    <div class="rank-row" style="top:62px"><span class="pos">3.</span><span class="name">Steffi36<i>Masterbiker</i></span><span class="face"><svg width="7" height="7" style="fill:#fff"><use href="#person"/></svg></span><span class="pts">321</span></div>
    <div class="rank-row" style="top:87px"><span class="pos">4.</span><span class="name">Sibille<i>Guru-biker</i></span><span class="face"><svg width="7" height="7" style="fill:#fff"><use href="#person"/></svg></span><span class="pts">211</span></div>
    <div class="rank-row" style="top:112px"><span class="pos">5.</span><span class="name">Martin89<i>Guru-biker</i></span><span class="face"><svg width="7" height="7" style="fill:#fff"><use href="#person"/></svg></span><span class="pts">177</span></div>
    <div class="rank-row" style="top:137px"><span class="pos">6.</span><span class="name">Thorsten66<i>Guru-biker</i></span><span class="face"><svg width="7" height="7" style="fill:#fff"><use href="#person"/></svg></span><span class="pts">167</span></div>
    <div class="rank-row" style="top:162px"><span class="pos">7.</span><span class="name">Sissi123<i>Hobbybiker</i></span><span class="face"><svg width="7" height="7" style="fill:#fff"><use href="#person"/></svg></span><span class="pts">154</span></div>
    <div class="rank-row" style="top:187px"><span class="pos">7.</span><span class="name">Sissi123<i>Hobbybiker</i></span><span class="face"><svg width="7" height="7" style="fill:#fff"><use href="#person"/></svg></span><span class="pts">154</span></div>
  </div>
</section>

</body>
</html>
```